Business Intelligence Application - Reporting Menu and Report Criteria Design

Looking for a fresh, effective and user friendly view for the menu structure and reporting criteria screen format for a business reporting application. Initial format completed, content structure is in place, but we need the 'wow' design.. as its a serious professional report/BI tool it has to fall within certain guidelines for clarity and graphics..but we want it to be slick, friendly, great user experience. There is a large amount of complex content to fit into a small space and we need it to be very inviting, modern and intuitive.. If interested, please review the attachment. We have live screens in operation, but feel these could be improved and looking forward to seeing what great creative suggestions could be made. Please review work done to date in the attached.. We are not looking for a total re-design of everything, all the basic business content/structure is there.. but tell us what we could do to improve this in terms of graphic design... particularly the criteria screens.. thanks!
Updates

Reason: Need a few more days to review designs - thanks for all submissions so far, we will make a selection shortly.

Target Market(s)

Business analysts, hotel operations teams, finance analysts hospitality industry

Industry/Entity Type

Hospitality

Coding

Coded - Design and coding required

Number of Pages Required

4 page

Font styles to use
Sans Serif
Other font styles liked:
• Candara, please see example in deck

Colors
3276b5
3176b5
0255a3
85acd3
33a6d7
cee9f5
85cae6

Requirements
Must have
• sharp clear, logical menu structure, (currently it has 'clicks to sub-menus, we need hover over, slide to sub-menus..) colour, styling.. and most focus on revision of criteria.. right now is somewhat heavy, cumbersome.. keep colour and friendly intuitive process steps.. its heavy analytical stuff.. best of luck!
Should not have
• No grey fonts on white or grey screens! many business apps are not readable or sharp.. or fonts are too small.. colourless, so please avoid that.. see our deck - sharp dark (navy) or black fonts on white, or light shading..

```html
<!DOCTYPE html>
<html lang="en">
<head>
<meta charset="utf-8">
<title>Silver Harbor Hotel &amp; Suites – Rooms Performance</title>
<link href="https://fonts.googleapis.com/css2?family=Signika:wght@400;500;600&family=Roboto+Condensed:wght@500&display=swap" rel="stylesheet">
<style>
:root{
  --page:#e6e6e6;
  --navy:#0d1640;
  --footer:#031536;
  --header-a:#233266;
  --header-b:#6d7db3;
  --tab-blue:#a8c1ea;
  --tab-grey:#d9d9d9;
  --tools:#666;
  --bar:#e3e3e3;
  --th:#a9bdd6;
  --th-line:#ffffff;
  --section:#9b9b9b;
  --label-a:#eef2f8;
  --label-b:#bccbdd;
  --cell-a:#ffffff;
  --cell-b:#dde6f1;
  --ink:#0d1a3a;
  --accent:#33a6d7;
}
*{box-sizing:border-box;margin:0;padding:0}
html,body{width:1200px;height:711px;overflow:hidden;background:var(--page)}
body{position:relative;font-family:"Signika",sans-serif;color:var(--ink)}
.app-header{position:absolute;left:11px;top:11px;width:1178px;height:53px;
  background:linear-gradient(90deg,var(--header-a),var(--header-b));display:flex;align-items:center;color:#fff}
.brand{display:flex;align-items:center;gap:12px;padding-left:22px;flex:1;font-size:17px;font-weight:500}
.brand-mark{width:30px;height:30px;background:#85cae6;border-radius:50%}
.header-cell{height:100%;display:flex;align-items:center;gap:12px;border-left:1px solid rgba(255,255,255,.35);padding:0 16px;font-size:11px;font-weight:500}
.user{width:140px}.date{width:134px;line-height:13px}.icon-only{width:53px;justify-content:center;padding:0}
.main-nav{position:absolute;left:11px;top:69px;width:1178px;height:30px;display:flex;gap:4px}
.nav-item{display:flex;align-items:center;justify-content:center;font-family:"Roboto Condensed",sans-serif;font-size:10.5px;font-weight:500;color:#fff;background:var(--navy)}
.nav-item.active{background:var(--tab-blue);color:var(--ink)}
.nav-item.muted{background:var(--tab-grey);color:var(--ink)}
.mascot{width:22px;height:22px;border-radius:50%;background:#c98a3c}
.tools-bar{position:absolute;left:11px;top:103px;width:1178px;height:30px;background:var(--bar);display:flex;align-items:center}
.tools-btn{width:71px;height:100%;background:var(--tools);color:#fff;display:flex;align-items:center;justify-content:center;gap:6px;font-family:"Roboto Condensed",sans-serif;font-size:10px}
.criteria{padding-left:25px;font-family:"Roboto Condensed",sans-serif;font-size:10px;color:var(--ink)}
.workspace{position:absolute;left:11px;top:133px;width:1178px;height:505px;background:#fff}
.report{position:absolute;left:0;top:31px;width:1178px;border-collapse:collapse;table-layout:fixed;font-size:12px;font-weight:500}
.report col.label{width:191px}.report col.total{width:77px}
.report th{background:var(--th);font-weight:500;height:23px;border-left:1px solid var(--th-line);font-size:12px}
.report thead tr:first-child th{border-bottom:1px solid var(--th-line)}
.report th.range{text-align:left;padding-left:25px;font-size:11px;line-height:13px;border-left:none}
.report td{height:22.94px;text-align:center;background:linear-gradient(var(--cell-a),var(--cell-b));font-size:10.5px;font-weight:600}
.report td.name{text-align:left;padding-left:25px;font-size:12px;font-weight:500;background:linear-gradient(90deg,var(--label-a),var(--label-b))}
.report td.tot{background:#f4f6f9}
.report tr.section td{background:#f0f0f0}
.report tr.section td.name{background:var(--section);color:#fff}
.app-footer{position:absolute;left:11px;top:638px;width:1178px;height:62px;background:var(--footer);display:flex;align-items:center;justify-content:center;gap:10px;color:#fff;font-size:16px;font-weight:500}
.footer-mark{width:22px;height:22px;background:var(--accent)}
</style>
</head>
<body>
<header class="app-header">
  <div class="brand"><span class="brand-mark"></span>Silver Harbor Hotel &amp; Suites</div>
  <div class="header-cell user">
    <svg width="22" height="24" viewBox="0 0 22 24"><circle cx="11" cy="7" r="6" fill="#fff"/><path d="M0 24c0-7 5-10 11-10s11 3 11 10z" fill="#fff"/></svg>Welcome Admin</div>
  <div class="header-cell date">
    <svg width="22" height="20" viewBox="0 0 22 20"><rect x="1" y="3" width="20" height="16" fill="none" stroke="#fff" stroke-width="2"/><rect x="1" y="3" width="20" height="4" fill="#fff"/><g fill="#fff"><rect x="5" y="10" width="3" height="2"/><rect x="10" y="10" width="3" height="2"/><rect x="15" y="10" width="3" height="2"/><rect x="5" y="14" width="3" height="2"/><rect x="10" y="14" width="3" height="2"/></g></svg>
    <span>Tuesday<br>October 3, 2017</span></div>
  <div class="header-cell icon-only"><svg width="20" height="22" viewBox="0 0 20 22"><path d="M3 16V9a7 7 0 0 1 14 0v7l2 2H1z" fill="#fff"/><circle cx="10" cy="20" r="2" fill="#fff"/></svg></div>
  <div class="header-cell icon-only"><svg width="24" height="24" viewBox="0 0 24 24"><path d="M7 5a9 9 0 1 0 10 0" fill="none" stroke="#fff" stroke-width="2.5" stroke-linecap="round"/><line x1="12" y1="2" x2="12" y2="11" stroke="#fff" stroke-width="2.5" stroke-linecap="round"/></svg></div>
</header>

<nav class="main-nav">
  <div class="nav-item" style="width:71px">ADMIN</div>
  <div class="nav-item" style="width:104px">MANAGEMENT</div>
  <div class="nav-item active" style="width:142px">ROOMS PERFORMANCE</div>
  <div class="nav-item muted" style="width:129px">REVENUE SUMMARY</div>
  <div class="nav-item active" style="width:112px">DEMAND &amp; RISK</div>
  <div class="nav-item muted" style="width:137px">INVENTORY ANALYSIS</div>
  <div class="nav-item muted" style="width:105px">PLACEHOLDER</div>
  <div class="nav-item muted" style="width:57px"><span class="mascot" role="img" aria-label="Mascot character icon"></span></div>
  <div class="nav-item" style="width:125px">PROPERTY SEARCH</div>
  <div class="nav-item" style="width:66px">INTEL</div>
  <div class="nav-item" style="width:90px">PLANNING</div>
</nav>

<div class="tools-bar">
  <div class="tools-btn"><svg width="18" height="18" viewBox="0 0 18 18"><path d="M2 2l14 14M16 2L2 16" stroke="#f0c040" stroke-width="2.5" stroke-linecap="round"/></svg>TOOLS</div>
  <div class="criteria">SELECTED REPORT LABEL CRITERIA</div>
</div>

<main class="workspace">
<table class="report">
  <colgroup><col class="label"><col class="total"><col span="12"></colgroup>
  <thead>
    <tr><th class="range" rowspan="2">Aug 16, 2017 - Sept 30, 2017 -<br>Aug 17, 2016 - Oct 1, 2016</th><th rowspan="2">Total</th>
      <th>Aug 16</th><th>Aug 17</th><th>Aug 18</th><th>Aug 19</th><th>Aug 20</th><th>Aug 21</th><th>Aug 22</th><th>Aug 23</th><th>Aug 24</th><th>Aug 25</th><th>Aug 26</th><th>Aug 27</th></tr>
    <tr><th>Wed</th><th>Thu</th><th>Fri</th><th>Sat</th><th>Sun</th><th>Mon</th><th>Tue</th><th>Wed</th><th>Thu</th><th>Fri</th><th>Sat</th><th>Sun</th></tr>
  </thead>
  <tbody>
    <tr class="section"><td class="name">Occupancy</td><td colspan="13"></td></tr>
    <tr><td class="name">Occupany Active Net</td><td class="tot">0.0%</td><td>0.0%</td><td>0.0%</td><td>0.0%</td><td>0.0%</td><td>0.0%</td><td>0.0%</td><td>0.0%</td><td>0.0%</td><td>0.0%</td><td>0.0%</td><td>0.0%</td><td>0.0%</td></tr>
    <tr><td class="name">Occupancy on the Books</td><td class="tot">0.0%</td><td>0.0%</td><td>0.0%</td><td>0.0%</td><td>0.0%</td><td>0.0%</td><td>0.0%</td><td>0.0%</td><td>0.0%</td><td>0.0%</td><td>0.0%</td><td>0.0%</td><td>0.0%</td></tr>
    <tr><td class="name">Occupancy Gap</td><td class="tot">0.0%</td><td>0.0%</td><td>0.0%</td><td>0.0%</td><td>0.0%</td><td>0.0%</td><td>0.0%</td><td>0.0%</td><td>0.0%</td><td>0.0%</td><td>0.0%</td><td>0.0%</td><td>0.0%</td></tr>
    <tr><td class="name">Net Available Rooms</td><td class="tot">0</td><td>0</td><td>0</td><td>0</td><td>0</td><td>0</td><td>0</td><td>0</td><td>0</td><td>0</td><td>0</td><td>0</td><td>0</td></tr>
    <tr class="section"><td class="name">Rooms &amp; Demand Risk</td><td colspan="13"></td></tr>
    <tr><td class="name">Active Rm Nights</td><td class="tot">0</td><td>0</td><td>0</td><td>0</td><td>0</td><td>0</td><td>0</td><td>0</td><td>0</td><td>0</td><td>0</td><td>0</td><td>0</td></tr>
    <tr><td class="name">Risk Ratio Rm Nights</td><td class="tot">0.0%</td><td>0.0%</td><td>0.0%</td><td>0.0%</td><td>0.0%</td><td>0.0%</td><td>0.0%</td><td>0.0%</td><td>0.0%</td><td>0.0%</td><td>0.0%</td><td>0.0%</td><td>0.0%</td></tr>
    <tr><td class="name">Active Avg Rm Rate</td><td class="tot">0.0</td><td>0.0</td><td>0.0</td><td>0.0</td><td>0.0</td><td>0.0</td><td>0.0</td><td>0.0</td><td>0.0</td><td>0.0</td><td>0.0</td><td>0.0</td><td>0.0</td></tr>
    <tr><td class="name">Risk Ratio Avg Rm Rate</td><td class="tot">0.0%</td><td>0.0%</td><td>0.0%</td><td>0.0%</td><td>0.0%</td><td>0.0%</td><td>0.0%</td><td>0.0%</td><td>0.0%</td><td>0.0%</td><td>0.0%</td><td>0.0%</td><td>0.0%</td></tr>
    <tr><td class="name">Active Rm Revenue</td><td class="tot">0</td><td>0</td><td>0</td><td>0</td><td>0</td><td>0</td><td>0</td><td>0</td><td>0</td><td>0</td><td>0</td><td>0</td><td>0</td></tr>
    <tr><td class="name">Risk Ratio Rm Revenue</td><td class="tot">0.0%</td><td>0.0%</td><td>0.0%</td><td>0.0%</td><td>0.0%</td><td>0.0%</td><td>0.0%</td><td>0.0%</td><td>0.0%</td><td>0.0%</td><td>0.0%</td><td>0.0%</td><td>0.0%</td></tr>
    <tr class="section"><td class="name">Occupancy</td><td colspan="13"></td></tr>
    <tr><td class="name">Rm Nts OTB CY Def</td><td class="tot">0</td><td>0</td><td>0</td><td>0</td><td>0</td><td>0</td><td>0</td><td>0</td><td>0</td><td>0</td><td>0</td><td>0</td><td>0</td></tr>
    <tr><td class="name">Rm Nts OTB Prior Def</td><td class="tot">0</td><td>0</td><td>0</td><td>0</td><td>0</td><td>0</td><td>0</td><td>0</td><td>0</td><td>0</td><td>0</td><td>0</td><td>0</td></tr>
    <tr><td class="name">Difference</td><td class="tot">0</td><td>0</td><td>0</td><td>0</td><td>0</td><td>0</td><td>0</td><td>0</td><td>0</td><td>0</td><td>0</td><td>0</td><td>0</td></tr>
    <tr><td class="name">% Variance</td><td class="tot">0.0%</td><td>0.0%</td><td>0.0%</td><td>0.0%</td><td>0.0%</td><td>0.0%</td><td>0.0%</td><td>0.0%</td><td>0.0%</td><td>0.0%</td><td>0.0%</td><td>0.0%</td><td>0.0%</td></tr>
  </tbody>
</table>
</main>

<footer class="app-footer"><span class="footer-mark"></span>RateWise</footer>
</body>
</html>
```